Dental hygiene website

I would like to design to website that both dental professionals and the public can get information. I would also like a shopping cart as well. The name of the company is called Velqind. We have a product called the fresca one. Delia is the Ceo. Marcus is the CIO. Oliver is the COO. We are based in Parkland, Fl. The site should have a clean modern look that possibly has a natural/nature/ocean theme. We believe in an overall healthy lifestyle. We would like links to twitter/instagram/facebook. i would like to make additions to my shopping cart when we bring on new products. I would also like the ability to add new staff bio/photos when we add employees. The site must be able to be edited by myself once we take ownership.

sorry for the delay. I just uploaded the company logo

Reason: I forced to travel for business. please make any last minute submissions using the logo i uploaded. i will choose on october 25th

```html
<!DOCTYPE html>
<html lang="en">
<head>
<meta charset="utf-8">
<title>Velqind – Dental Hygiene</title>
<link href="https://fonts.googleapis.com/css2?family=Open+Sans:ital,wght@0,300;0,400;0,600;0,700;0,800;1,400;1,600&display=swap" rel="stylesheet">
<style>
:root{
  --blue:#2aa7e6;
  --blue-dark:#1b8fd0;
  --ink:#2c2c2c;
  --muted:#7a7a7a;
  --light:#f1f1f1;
  --dark:#1c1c1c;
  --darker:#121212;
  --green:#3fb58a;
  --white:#ffffff;
}
*{box-sizing:border-box;margin:0;padding:0}
html,body{width:1200px;height:2884px;overflow:hidden}
body{font-family:"Open Sans",Arial,sans-serif;color:var(--ink);background:var(--white);position:relative}
.wrap{width:1000px;margin:0 auto;position:relative}

/* top strip */
.topstrip{height:24px;background:var(--white);border-bottom:1px solid #eee}
.topstrip .wrap{display:flex;justify-content:space-between;align-items:center;height:24px;font-size:10px;color:var(--muted)}

/* header */
.site-header{height:64px;background:var(--white)}
.site-header .wrap{display:flex;align-items:center;height:64px}
.brand{display:flex;align-items:center;gap:8px;font-size:22px;font-weight:600;color:#5a6470;letter-spacing:2px}
.brand-dot{width:14px;height:14px;border-radius:50%;background:var(--blue)}
.main-nav{display:flex;gap:26px;margin-left:auto;font-size:12px;color:#555}
.main-nav .active{color:var(--blue);border-bottom:2px solid var(--blue);padding-bottom:4px}
.social{display:flex;gap:6px;margin-left:34px}
.social span{width:18px;height:18px;background:#555;border-radius:2px}
.cart{margin-left:18px;display:flex;align-items:center;gap:6px;font-size:11px;color:#555}
.cart b{display:inline-block;width:26px;height:22px;background:var(--blue);border-radius:2px}

/* hero */
.hero{position:relative;height:312px;background:linear-gradient(100deg,#9a9fa6 0%,#c9ccd0 40%,#e3d9d2 70%,#b9bdc3 100%)}
.hero-photo{position:absolute;inset:0}
.hero .wrap{padding-top:40px}
.hero h1{font-size:50px;font-weight:800;color:var(--white);line-height:1.05;letter-spacing:1px}
.hero h2{font-size:34px;font-weight:300;color:var(--white);line-height:1.2;margin-top:6px}
.btn{display:inline-block;background:var(--blue);color:var(--white);font-size:12px;font-weight:700;padding:10px 22px;text-transform:uppercase;letter-spacing:.5px}
.hero .btn{margin-top:26px}

/* info boxes */
.info-band{background:var(--light);height:240px;padding-top:48px}
.info-band .wrap{display:flex;gap:20px}
.info-box{flex:1;background:var(--blue);color:var(--white);height:152px;padding:20px 22px}
.info-box h3{font-size:15px;font-weight:700;text-transform:uppercase;line-height:1.25}
.info-box p{font-size:11px;line-height:1.55;margin-top:10px;opacity:.9}

/* product */
.product{height:720px;padding-top:50px}
.section-title{font-size:30px;font-weight:400;color:var(--ink);text-transform:uppercase}
.product-grid{display:flex;margin-top:0}
.product-left{width:470px}
.product-shot{width:380px;height:300px;margin-top:30px;background:radial-gradient(circle at 50% 50%,#e6ecf1 0%,#ffffff 70%)}
.register-link{display:block;margin-top:22px;margin-left:130px;font-size:11px;font-weight:700;color:#d23b3b;text-transform:uppercase}
.product-right{flex:1;padding-top:0}
.product-name{font-size:40px;font-style:italic;font-weight:600;color:var(--blue);margin-top:-6px}
.features h4{font-size:24px;font-weight:700;margin-top:22px}
.features ul{list-style:none;margin-top:8px}
.features li,.benefits li{font-size:17px;line-height:1.55}
.features li::before,.benefits li::before{content:"•";margin-right:10px}
.register-title{font-size:36px;font-weight:700;color:var(--blue);margin-top:30px;line-height:1.1}
.register-title span{display:block;font-size:28px;font-weight:600;font-style:italic}
.benefits{list-style:none;margin-top:12px;color:#444}
.goal{display:flex;align-items:center;margin-top:30px}
.goal p{width:560px;font-size:28px;font-style:italic;color:var(--blue);text-align:center;line-height:1.3}
.goal-photo{width:200px;height:230px;margin-left:60px;background:linear-gradient(180deg,#f2f2f2,#d9dde2)}

/* about band */
.about{position:relative;height:600px;background:linear-gradient(180deg,#3a3a3a 0%,#222 60%,#1a1a1a 100%);color:var(--white);text-align:center;padding-top:62px}
.about .section-title{color:var(--white);font-weight:600}
.about .lead{font-size:15px;font-weight:700;margin-top:10px}
.about .sub{font-size:12px;margin-top:4px;opacity:.85}
.cards{display:flex;justify-content:center;gap:22px;margin-top:54px}
.card{width:128px;text-align:left}
.card-img{height:128px;background:linear-gradient(180deg,#ffffff,#e1e9ef);border:4px solid var(--white)}
.card p{font-size:11px;font-weight:700;line-height:1.3;margin-top:8px;text-transform:uppercase}
.card small{display:block;font-size:9px;font-weight:400;opacity:.8;text-transform:none}

/* topics */
.topics{height:400px;padding-top:32px}
.topic-grid{display:flex;gap:28px;margin-top:22px}
.topic{flex:1}
.topic-img{height:186px}
.topic h5{font-size:12px;font-weight:700;color:var(--blue);text-transform:uppercase;margin-top:12px;line-height:1.3}
.topic .date{font-size:9px;color:var(--muted);margin-top:4px}
.topic p{font-size:10px;color:var(--muted);line-height:1.5;margin-top:6px}

/* footer */
.site-footer{height:400px;background:var(--dark);color:#cfcfcf;padding-top:42px}
.site-footer .wrap{display:flex}
.foot-info{width:520px}
.foot-info .brand{color:var(--white);font-size:20px}
.foot-info .about-text{font-size:11px;line-height:1.6;margin-top:22px;width:280px}
.contact-list{list-style:none;margin-top:24px;font-size:11px}
.contact-list li{display:flex;align-items:center;gap:10px;margin-bottom:8px}
.contact-list svg{width:12px;height:12px}
.contact-form{width:480px;display:grid;grid-template-columns:1fr 1fr;gap:12px;margin-top:40px;align-content:start}
.field{height:30px;background:#2e2e2e;border:1px solid #3a3a3a;font-size:10px;color:#888;padding:8px 10px}
.field.wide{grid-column:1/3}
.field.msg{height:120px}
.form-actions{grid-column:1/3;display:flex;justify-content:space-between;margin-top:20px}
.form-actions span{width:120px;height:30px;font-size:12px;color:var(--white);display:flex;align-items:center;justify-content:center}
.reset{background:var(--green)}
.submit{background:var(--blue)}
.copyright{position:absolute;left:0;top:2844px;width:1200px;height:40px;background:var(--darker);color:#bbb;font-size:11px;text-align:center;line-height:40px}
</style>
</head>
<body>

<div class="topstrip">
  <div class="wrap">
    <span>Clean smiles, naturally – care for every day</span>
    <span>Support: (954) 555-0182</span>
  </div>
</div>

<header class="site-header">
  <div class="wrap">
    <div class="brand"><span class="brand-dot"></span>VELQIND</div>
    <nav class="main-nav">
      <span class="active">Home</span><span>About</span><span>Product</span><span>Dental Testimonials</span><span>Dental Health Topics</span><span>Contact Us</span>
    </nav>
    <div class="social"><span></span><span></span><span></span></div>
    <div class="cart">Cart (0) <b></b></div>
  </div>
</header>

<section class="hero">
  <div class="hero-photo" role="img" aria-label="Dentist treating a smiling patient in a bright dental clinic"></div>
  <div class="wrap">
    <h1>ENHANCE YOUR<br>PERFORMANCE...</h1>
    <h2>AND YOUR PATIENT'S<br>COMFORT</h2>
    <span class="btn">Find out more about us</span>
  </div>
</section>

<section class="info-band">
  <div class="wrap">
    <div class="info-box"><h3>How to choose a great dentist</h3><p>Look for gentle care, clear advice and a clinic that treats your whole family with patience and respect.</p></div>
    <div class="info-box"><h3>The costs of dental care</h3><p>Regular cleanings and checkups cost far less than repairs. Plan ahead and keep your smile healthy.</p></div>
    <div class="info-box"><h3>When should you consider braces?</h3><p>Crowded or crooked teeth can affect chewing and hygiene. Ask your dentist about the best timing.</p></div>
  </div>
</section>

<section class="product">
  <div class="wrap">
    <div class="product-grid">
      <div class="product-left">
        <h2 class="section-title">Our Product</h2>
        <div class="product-shot" role="img" aria-label="Fresca One handheld prophy handpiece with blue disposable angle"></div>
        <span class="register-link">Register now</span>
      </div>
      <div class="product-right">
        <div class="product-name">Fresca One</div>
        <div class="features">
          <h4>Features:</h4>
          <ul>
            <li>Accepts all standard prophy angles</li>
            <li>Quick disconnect nosecone</li>
            <li>360-degree swivel</li>
          </ul>
        </div>
        <div class="register-title">Register your product<span>and get great benefits</span></div>
        <ul class="benefits">
          <li>Gain access to the latest savings</li>
          <li>Promotions</li>
          <li>Product news &amp; more</li>
        </ul>
      </div>
    </div>
    <div class="goal">
      <p>Our goal is to make sure you leave<br>with a smile on your face!</p>
      <div class="goal-photo" role="img" aria-label="Smiling dental hygienist in a white coat pointing to the side"></div>
    </div>
  </div>
</section>

<section class="about">
  <h2 class="section-title">About Our Product</h2>
  <p class="lead">NOTHING COMPARES TO OUR UNIQUE FRESCA ONE TECHNOLOGY.</p>
  <p class="sub">After 20 years, we're still the #1 recommended name in oral hygiene tools by dental professionals nationwide.</p>
  <div class="cards">
    <div class="card"><div class="card-img" role="img" aria-label="Row of Fresca One toothbrushes"></div><p><small>Fresca One</small>Toothbrushes</p></div>
    <div class="card"><div class="card-img" role="img" aria-label="Replacement brush heads"></div><p><small>Fresca One</small>Brush heads</p></div>
    <div class="card"><div class="card-img" role="img" aria-label="Prophy handpiece and angles"></div><p><small>Fresca One</small>Airflows</p></div>
    <div class="card"><div class="card-img" role="img" aria-label="Bright white smile close-up"></div><p><small>Fresca One</small>Whitening</p></div>
  </div>
</section>

<section class="topics">
  <div class="wrap">
    <h2 class="section-title">Dental Health Topics</h2>
    <div class="topic-grid">
      <div class="topic">
        <div class="topic-img" role="img" aria-label="Close-up of a bright smile" style="background:linear-gradient(135deg,#f3d6cf,#ffffff 60%,#e9e9e9)"></div>
        <h5>How to quickly whiten your teeth for a good smile</h5>
        <div class="date">Posted on October 12, 2016</div>
        <p>Simple daily habits and the right tools can lift stains and keep your teeth bright between visits.</p>
      </div>
      <div class="topic">
        <div class="topic-img" role="img" aria-label="Dentist examining a patient in a clinic chair" style="background:linear-gradient(135deg,#d7e6ee,#b9cfdc)"></div>
        <h5>How to keep your gums healthy</h5>
        <div class="date">Posted on October 08, 2016</div>
        <p>Gentle brushing, daily flossing and regular cleanings protect your gums from early disease.</p>
      </div>
      <div class="topic">
        <div class="topic-img" role="img" aria-label="Child smiling at a pediatric dental visit" style="background:linear-gradient(135deg,#e6f1e2,#cfe3ef)"></div>
        <h5>The ultimate beginner pediatric care</h5>
        <div class="date">Posted on October 02, 2016</div>
        <p>Start good habits early with soft brushes, fun routines and a first visit by age one.</p>
      </div>
    </div>
  </div>
</section>

<footer class="site-footer">
  <div class="wrap">
    <div class="foot-info">
      <div class="brand"><span class="brand-dot"></span>VELQIND</div>
      <p class="about-text">The Fresca One prophy handpiece is built for comfort and precision, helping dental teams deliver a gentler clean in less time.</p>
      <ul class="contact-list">
        <li><svg viewBox="0 0 12 12"><circle cx="6" cy="6" r="5" fill="#2aa7e6"/></svg>Fresca One</li>
        <li><svg viewBox="0 0 12 12"><path d="M3 1h2l1 3-1.5 1a6 6 0 0 0 2.5 2.5L8 6l3 1v2a2 2 0 0 1-2 2A8 8 0 0 1 1 3a2 2 0 0 1 2-2z" fill="#cfcfcf"/></svg>(954) 555-0182 &nbsp; (954) 555-0197</li>
        <li><svg viewBox="0 0 12 12"><rect x="1" y="3" width="10" height="7" fill="none" stroke="#cfcfcf"/><path d="M1 3l5 4 5-4" fill="none" stroke="#cfcfcf"/></svg>hello@velqind.com</li>
      </ul>
    </div>
    <div class="contact-form">
      <div class="field">Name</div>
      <div class="field">Last name</div>
      <div class="field">Email</div>
      <div class="field">Phone</div>
      <div class="field wide msg">Message</div>
      <div class="form-actions"><span class="reset">Reset</span><span class="submit">Submit</span></div>
    </div>
  </div>
</footer>
<div class="copyright">Copyright 2016 © Velqind. All right reserved.</div>

</body>
</html>
```